Marine Services Letterhead design

We need a letterhead design for an Australian owned company in Victoria named Q+Q Harbour Works Pty Ltd. We provide linesmen and launches to assist the large ships that come into port.
Our colour is orange.
The final design should have a strong nautical theme and communicate safety and reliability.
I would like to use the letter head on invoices so it should print to pdf well.

Target Market(s)

Owners and representatives of shipping companies. It is not for general public

Industry/Entity Type

Nautical

Requirements
Must have
• A shipping theme, not overly complicated, featuring safety orange colours but not all orange of course.
The letterhead should just sit at the top of the page so I can use for invoices.
Nice to have
• Something elegant and stylish
Should not have
• cartoons or pop art

```html
<!DOCTYPE html>
<html lang="en">
<head>
<meta charset="utf-8">
<title>Q+Q Harbour Works Pty Ltd — Letterhead</title>
<link href="https://fonts.googleapis.com/css2?family=Exo+2:wght@400;600&display=swap" rel="stylesheet">
<style>
  :root {
    --backdrop: #ebebeb;
    --paper: #f8f8f8;
    --ink: #6a6a6a;
    --ink-soft: #8a8a8a;
    --sea-green: #8fb59b;
    --safety-orange: #e0a45f;
    --brand-orange: #e39a4a;
    --signature-tone: #d8d8d8;
  }
  * { box-sizing: border-box; margin: 0; padding: 0; }
  html, body {
    width: 1200px; height: 1000px; overflow: hidden;
    background: var(--backdrop);
    font-family: "Exo 2", sans-serif;
  }
  .letterhead {
    position: absolute; left: 267px; top: 30px;
    width: 665px; height: 940px;
    background: var(--paper);
    box-shadow: 0 2px 10px rgba(0,0,0,0.08);
  }
  .brand-mark {
    position: absolute; top: 78px; left: 0; right: 0;
    display: flex; justify-content: center; align-items: center; gap: 8px;
  }
  .brand-mark__square { width: 14px; height: 14px; background: var(--brand-orange); }
  .brand-mark__name {
    font-size: 17px; font-weight: 600; color: var(--brand-orange); letter-spacing: 0.5px;
  }
  .letter-body {
    position: absolute; top: 170px; left: 150px; right: 60px;
    font-size: 8.6px; line-height: 1.65; color: var(--ink);
  }
  .letter-body p { margin-bottom: 22px; }
  .letter-body .salutation { margin-bottom: 12px; }
  .letter-body .closing { margin-bottom: 0; }
  .signature {
    position: absolute; top: 575px; left: 400px;
    width: 150px; height: 40px;
    background: linear-gradient(90deg, rgba(216,216,216,0) 0%, var(--signature-tone) 50%, rgba(216,216,216,0) 100%);
    border-radius: 20px; opacity: 0.6;
  }
  .band-green {
    position: absolute; left: 0; top: 815px; width: 305px; height: 8px;
    background: var(--sea-green);
  }
  .band-orange {
    position: absolute; left: 305px; right: 0; bottom: 0; height: 10px;
    background: var(--safety-orange);
  }
  .footer-details {
    position: absolute; left: 232px; top: 838px;
    color: var(--ink);
  }
  .footer-details__company {
    font-size: 10.5px; font-weight: 600; color: var(--brand-orange);
    margin-left: 40px; margin-bottom: 4px;
  }
  .footer-details__contact {
    display: flex; gap: 10px; font-size: 7.5px; align-items: center;
  }
  .footer-details__contact span { display: flex; align-items: center; gap: 3px; }
  .footer-details__contact svg { width: 8px; height: 8px; fill: var(--sea-green); }
</style>
</head>
<body>
  <main class="letterhead">
    <header class="brand-mark">
      <span class="brand-mark__square"></span>
      <span class="brand-mark__name">Q+Q Harbour Works</span>
    </header>

    <section class="letter-body">
      <p class="salutation">Dear Client,</p>
      <p>Lorem ipsum dolor sit amet, consectetur adipiscing elit. Nulla sodales nisi vitae lorem ipsum dolor sit amet, consectetur adipiscing elit. Suspendisse feugiat eros nisl, a facilisis risus eleifend sed. Aliquam mauris enim, fermentum eu lacinia sit amet, laoreet eu leo. Nullam eleifend nulla in libero tristique, ac vulputate odio tincidunt. Etiam non condimentum tortor. Integer suscipit neque nec odio porttitor cursus. Phasellus a sapien blandit, suscipit justo id, condimentum ante. Morbi tristique justo risus, id mattis dui molestie ut. Nullam volutpat ut quam commodo faucibus. Pellentesque urna est, interdum in elit quis, pharetra elementum orci. Nam pharetra velit molestie justo placerat scelerisque.</p>
      <p>Nulla tincidunt molestie libero vel pretium. Donec condimentum nulla sit amet risus semper imperdiet. Duis congue eros nec diam blandit, et pellentesque sapien auctor. Curabitur iaculis enim lectus, in imperdiet mauris mattis eget. Etiam ac ornare metus. Mauris risus leo, egestas at dolor a, ultrices adipiscing est. Nunc faucibus scelerisque mollis. Pellentesque aliquet mauris tellus, id dignissim risus viverra et. Mauris venenatis lobortis eros. Nam id diam in ligula malesuada feugiat. Cras turpis felis, aliquet id mauris elementum, feugiat ultrices nisl.</p>
      <p>Nullam auctor venenatis metus, eu pulvinar sapien dapibus non. Cum sociis natoque penatibus et magnis dis parturient montes, nascetur ridiculus mus. Praesent sed lorem eget tortor volutpat dictum vel vel ipsum. Morbi ac mauris sed elit dictum volutpat. Morbi pulvinar non nisi in ultrices. Pellentesque quis mi in risus eleifend adipiscing.</p>
      <p class="closing">Best regards,</p>
    </section>

    <div class="signature" role="img" aria-label="Handwritten signature of the sender"></div>

    <div class="band-green"></div>
    <div class="band-orange"></div>

    <footer class="footer-details">
      <p class="footer-details__company">Q+Q Harbour Works Pty Ltd</p>
      <div class="footer-details__contact">
        <span>
          <svg viewBox="0 0 10 10" aria-hidden="true"><path d="M5 0a3.5 3.5 0 0 0-3.5 3.5C1.5 6 5 10 5 10s3.5-4 3.5-6.5A3.5 3.5 0 0 0 5 0zm0 5a1.5 1.5 0 1 1 0-3 1.5 1.5 0 0 1 0 3z"/></svg>
          PO Box 412 Seacliff Bay 3999
        </span>
        <span>
          <svg viewBox="0 0 10 10" aria-hidden="true"><path d="M2 0.5l2 2-1 1.3c.6 1.3 1.6 2.3 2.9 2.9L7.2 5.7l2.3 2-1 1.8C4.5 9.3.7 5.5.4 1.5z"/></svg>
          1300 555 018
        </span>
        <span>
          <svg viewBox="0 0 10 10" aria-hidden="true"><path d="M2 0h5v3H2zM0 3.5h10V8H8v2H2V8H0zm3 3v2.5h4V6.5z"/></svg>
          0355 501 234
        </span>
      </div>
    </footer>
  </main>
</body>
</html>
```